Online Course Web Pages

Seeking web designer to design a 3 page website related to the promotion of an online course and a square graphic for the student login portal. Pages to include:
1) Opt-in page to request information on online course
2) Online course sales page with enrollment order form
3) Online course enrollment confirmation page
4) Online course login portal page design-- requires 600 x 600 graphic design
TARGET AUDIENCE: (for stock photo reference)
- Entry-level employees: Front-desk staff, servers, housekeeping staff, etc.
- Mid-level managers: Assistant managers, supervisors, department heads
- Experienced professionals: General managers, directors, executives
- Students: Hospitality, tourism, and leisure management students
- Recent graduates: Seeking entry-level positions in the industry
- Career changers: Individuals looking to transition into the hospitality, tourism, and leisure industry
- Hotel and accommodation professionals: General managers, hotel managers, front office managers, sales managers, revenue managers
- Restaurant and food service professionals: General managers, executive chefs, food and beverage directors, sommeliers
- Event planners and managers
- Tour operators and travel agents
- Spa and wellness professionals
- Customer service representatives
PRIMARY BRAND COLORS:
BACKGROUND - HEX CODE #FFDE59; TEXT - #000000; ACCENT #FFFFFF
COMPLEMENTARY COLORS (highlighter style colors)
sky #72EEFF; lime #C1FF72; stop sign #FF0000
DESIGN INSTRUCTIONS:
Webpages should incorporate the color palette used in the Zumbrava logo. Design tone should be fun, upbeat and modern. Stock images of happy workers and professionals throughout the hospitality, leisure and tourism industries should be incorporated throughout. Related stock images showing people or related items in the colors used in the logo are preferred. See sample web design, logo and web copy attached for additional reference.
ATTACHED FILES:
- Copy docs
- Logo
- Sample web page designs for optional reference
PROJECT ADJUSTMENT: I am seeking assistance with designing web pages to promote an online course. I am changing my original request for 4 web pages to just 2 web pages. Please reference the web brief and copy originally submitted for assistance with this project. Relevant copy for web page designs include: Lead Magnet Web Page Copy-- https://files.plumvetta.net/sheet/p/84QwRRTmmUkaLe7y3Hoxq-NbVCanWeP_k8Ztq-Lm_jRDX/view?ref=sharing; and Sales Page web page copy-- https://files.plumvetta.net/sheet/p/7yanudsoP5tcVbmqo-VhpwGRwqFhy-Jd3ap4Hx/view?ref=sharing.

```html
<!DOCTYPE html>
<html lang="en">
<head>
<meta charset="utf-8">
<title>Online Course Lead Magnet – Zumbrava</title>
<link rel="stylesheet" href="https://fonts.googleapis.com/css2?family=Barlow+Semi+Condensed:wght@400;500&family=Arimo:wght@400;700&display=swap">
<style>
:root{
  --stage:#cfcfcf;
  --paper:#ffffff;
  --ink:#1c1b3a;
  --text:#222222;
  --black:#000000;
  --brand:#ffde59;
  --panel:#f3f3f3;
  --field:#ffffff;
  --muted:#555555;
}
*{box-sizing:border-box;margin:0;padding:0}
html,body{width:1200px;height:3656px;overflow:hidden}
body{background:var(--stage);font-family:"Arimo",Arial,sans-serif;color:var(--text)}
.page{position:absolute;left:131px;top:116px;width:939px;height:3427px;background:var(--paper);overflow:hidden}
.abs{position:absolute}
.photo{position:absolute}
.display{font-family:"Barlow Semi Condensed","Arial Narrow",sans-serif;font-weight:400;color:var(--ink);text-align:center;line-height:1.15}
.copy{font-size:8px;line-height:15px;text-align:center;color:var(--text)}
.btn{position:absolute;background:var(--brand);color:var(--black);font-size:8px;font-weight:700;letter-spacing:.2px;display:flex;align-items:center;justify-content:center;text-transform:uppercase}

/* header */
.brand-mark{position:absolute;display:flex;align-items:center;gap:6px;font-family:"Barlow Semi Condensed",sans-serif;font-weight:500;font-size:15px;color:var(--black)}
.brand-mark .sq{width:14px;height:14px;background:var(--brand);border:2px solid var(--black)}
.site-title{position:absolute;left:153px;top:22px;font-family:"Barlow Semi Condensed",sans-serif;font-size:33px;color:var(--ink)}

/* form */
.form-panel{position:absolute;background:var(--black);color:#fff}
.form-panel h2{position:absolute;font-family:"Barlow Semi Condensed",sans-serif;font-weight:400;font-size:32px;color:#fff}
.form-panel .intro{position:absolute;font-size:7.5px;line-height:12px;color:#fff}
.field{position:absolute;background:var(--field);border-radius:2px;font-size:7px;color:#333;display:flex;align-items:center;padding-left:9px}
.field .chev{position:absolute;right:9px;top:50%;width:5px;height:5px;border-right:1px solid #888;border-bottom:1px solid #888;transform:translateY(-70%) rotate(45deg)}
.form-panel .note{position:absolute;font-size:7px;color:#fff}
.form-panel .fine{position:absolute;font-size:6.5px;line-height:10px;color:#fff}

/* focus grid */
.focus-img{position:absolute;width:126px;height:144px}
.focus-title{position:absolute;font-family:"Barlow Semi Condensed",sans-serif;font-size:14px;color:var(--ink)}
.focus-text{position:absolute;font-size:7.5px;line-height:15px;width:200px}

/* audience */
.aud-icon{position:absolute;width:20px;height:20px}
.aud-text{position:absolute;font-size:7.5px;line-height:14px;width:180px}
</style>
</head>
<body>
<main class="page">

  <!-- header -->
  <header>
    <div class="brand-mark" style="left:78px;top:32px"><span class="sq"></span>Zumbrava</div>
    <h1 class="site-title">Online Course Lead Magnet</h1>
    <div class="photo" role="img" aria-label="Bunch of green onions" style="left:705px;top:0;width:234px;height:62px;background:linear-gradient(160deg,#ffffff 10%,#9fcf6a 45%,#4f8d2c 70%,#ffffff 95%)"></div>
  </header>

  <!-- hero -->
  <section class="hero">
    <div class="photo" role="img" aria-label="Two chefs preparing food together in a bright kitchen" style="left:0;top:81px;width:499px;height:407px;background:linear-gradient(120deg,#e9e7e3 0%,#cdc3b6 40%,#8b6a55 70%,#e4ddd4 100%)"></div>
    <div class="photo" role="img" aria-label="Bright kitchen shelves" style="left:854px;top:81px;width:85px;height:407px;background:linear-gradient(180deg,#eeeeee,#d6d6d6)"></div>
    <div class="form-panel" style="left:499px;top:81px;width:355px;height:407px">
      <h2 style="left:42px;top:18px">Get Started!</h2>
      <p class="intro" style="left:42px;top:62px;width:240px">Craving a thriving, high-paying career in hospitality, leisure, or tourism? You're not alone.</p>
      <div class="field" style="left:42px;top:104px;width:276px;height:30px">Online Course Lead Magnet<span class="chev"></span></div>
      <div class="field" style="left:42px;top:150px;width:133px;height:30px">First Name</div>
      <div class="field" style="left:185px;top:150px;width:133px;height:30px">Last Name</div>
      <div class="field" style="left:42px;top:196px;width:276px;height:30px">Email</div>
      <div class="field" style="left:42px;top:242px;width:276px;height:30px">Phone</div>
      <p class="note" style="left:42px;top:283px">Craving a thriving, high-paying career in hospitality</p>
      <div class="btn" style="left:42px;top:307px;width:276px;height:31px">Learn More</div>
      <p class="fine" style="left:42px;top:351px;width:276px">Craving a thriving, high-paying career in hospitality, leisure, or tourism? You're not alone. With millions of new jobs on the horizon, opportunities in the hospitality industry have never been more promising.</p>
    </div>
  </section>

  <!-- intro -->
  <section class="intro-section">
    <div class="photo" role="img" aria-label="Plate of spaghetti with tomatoes" style="left:-60px;top:580px;width:185px;height:258px;border-radius:50%;background:radial-gradient(circle,#e8c27a 0%,#c9782f 40%,#1a1a1a 62%,#ffffff 72%)"></div>
    <div class="photo" role="img" aria-label="Red bell pepper" style="left:743px;top:629px;width:196px;height:192px;background:radial-gradient(ellipse at 55% 55%,#d8201a 0%,#b81410 45%,#ffffff 72%)"></div>
    <h2 class="display abs" style="left:0;width:939px;top:585px;font-size:31px">A Thriving Career In Hospitality, Leisure<br>&amp; Tourism Starts Here…#Zumbrava</h2>
    <p class="copy abs" style="left:195px;width:550px;top:671px">Craving a thriving, high-paying career in hospitality, leisure, or tourism? You're not alone. With millions of new jobs on the horizon, opportunities in the hospitality industry have never been more promising. High-paying roles in hotel management, event planning, and luxury travel services are set to generate six-figure incomes like never before. BUT DO YOU HAVE WHAT IT TAKES TO RISE TO THE TOP?</p>
    <p class="copy abs" style="left:0;width:939px;top:736px">If not then #Zumbrava can help you get there.</p>
    <div class="btn" style="left:406px;top:776px;width:126px;height:31px">Request Information</div>
  </section>

  <!-- chef banner -->
  <section class="weapon">
    <div class="photo" role="img" aria-label="Chef in white uniform tasting pasta at a counter" style="left:81px;top:894px;width:771px;height:319px;background:linear-gradient(90deg,#ececec 0%,#e2e2e2 40%,#cfd3dc 52%,#e6e6e6 62%,#ececec 100%)"></div>
    <div class="photo" role="img" aria-label="Glazed barbecue ribs" style="left:0;top:1205px;width:240px;height:156px;background:radial-gradient(ellipse at 45% 45%,#9a3f1c 0%,#6d2a12 45%,#ffffff 72%)"></div>
    <div class="photo" role="img" aria-label="Halved avocados" style="left:790px;top:1190px;width:149px;height:242px;background:radial-gradient(ellipse at 50% 45%,#e5e08a 0%,#6f8f2a 45%,#ffffff 72%)"></div>
    <h2 class="display abs" style="left:0;width:939px;top:1279px;font-size:30px">#Zumbrava Is Your Secret Weapon To<br>WIN-WIN-WIN No Matter What!</h2>
    <p class="copy abs" style="left:165px;width:610px;top:1373px">#Zumbrava is your comprehensive online program designed to propel your career in hospitality, leisure, or tourism. From crafting the perfect resume to mastering leadership skills, we'll equip you with the tools to excel. Our program empowers you to not only survive but thrive in this dynamic industry. With 50 years of experience and a proven track record of success, #Zumbrava has helped more than 500 professionals achieve higher salaries, prestigious job titles, and fulfilling careers. A well-defined career path isn't just about job satisfaction – it's about building a life you love. Let us help you achieve your full potential and career dreams.</p>
    <p class="copy abs" style="left:165px;width:610px;top:1447px">#Zumbrava is your comprehensive online program designed to propel your career in hospitality, leisure, or tourism. From crafting the perfect resume to mastering leadership skills, we'll equip you with the tools to excel. Our program empowers you to not only survive but thrive in this dynamic industry.</p>
  </section>

  <!-- program focus -->
  <section class="focus">
    <h2 class="display abs" style="left:0;width:939px;top:1575px;font-size:30px">Our Program Focuses On</h2>

    <div class="focus-img photo" role="img" aria-label="Chef plating a dish on a wooden board" style="left:81px;top:1635px;background:linear-gradient(140deg,#d9cfc0,#8a6a48,#3f3f2a)"></div>
    <h3 class="focus-title" style="left:246px;top:1667px">Mastering Customer Service</h3>
    <p class="focus-text" style="left:246px;top:1693px">Gain advanced skills to enhance guest experiences and build lasting relationships with our culturally relevant training, which transforms everyday tasks into exceptional interactions.</p>

    <div class="focus-img photo" role="img" aria-label="Roasted rack of lamb with vegetables" style="left:492px;top:1635px;background:linear-gradient(140deg,#f2eee8,#8f5a3a,#d57b2c)"></div>
    <h3 class="focus-title" style="left:657px;top:1667px">Achieving Higher Salaries</h3>
    <p class="focus-text" style="left:657px;top:1693px">Reach your earning potential with targeted career development strategies.</p>

    <div class="focus-img photo" role="img" aria-label="Hands slicing fresh salmon" style="left:81px;top:1809px;background:linear-gradient(140deg,#2f2c28,#8a6a55,#e07a4a)"></div>
    <h3 class="focus-title" style="left:246px;top:1843px">Securing Better Job Titles</h3>
    <p class="focus-text" style="left:246px;top:1869px">Position yourself for roles that reflect your skills and ambitions.</p>

    <div class="focus-img photo" role="img" aria-label="Pouring golden sauce over a dessert" style="left:492px;top:1809px;background:linear-gradient(140deg,#f4f1ea,#f3d27a,#e8a53a)"></div>
    <h3 class="focus-title" style="left:657px;top:1843px">Making A Lasting Impact</h3>
    <p class="focus-text" style="left:657px;top:1869px">Making a Lasting Impact: Transform your work into a meaningful mission within the industry.</p>

    <div class="btn" style="left:395px;top:1990px;width:148px;height:31px">Request Information</div>
  </section>

  <!-- chance -->
  <section class="chance">
    <div class="photo" role="img" aria-label="Fresh green lettuce leaves" style="left:-20px;top:2128px;width:300px;height:440px;background:radial-gradient(ellipse at 30% 50%,#8fcf4a 0%,#5fa030 40%,#ffffff 70%)"></div>
    <div class="photo" role="img" aria-label="Broccoli florets" style="left:590px;top:2090px;width:349px;height:360px;background:radial-gradient(ellipse at 70% 40%,#4f8f2c 0%,#76b046 35%,#ffffff 68%)"></div>
    <div class="abs" style="left:81px;top:2152px;width:768px;height:319px;background:var(--panel)"></div>
    <h2 class="display abs" style="left:81px;width:768px;top:2220px;font-size:31px">Don’t Leave Your Career To Chance</h2>
    <p class="copy abs" style="left:205px;width:520px;top:2272px">In the competitive fields of hospitality, leisure, and tourism, mastering customer service is crucial for career advancement. Without top-notch training, your growth could be left to chance. Limited skills in this area can stifle progress, increase job insecurity, and lead to missed opportunities. Our #Zumbrava program ensures you not only navigate but excel in your career by focusing on customer service mastery – an indispensable skillset that can't be overlooked or underdeveloped. If you've felt stuck, underpaid, or uncertain about your next move, #Zumbrava will equip you with the expertise to secure the career success you deserve.</p>
    <div class="btn" style="left:395px;top:2373px;width:148px;height:31px">Request Information</div>
  </section>

  <!-- audience -->
  <section class="audience">
    <h2 class="display abs" style="left:0;width:939px;top:2616px;font-size:30px">Who Is #Zumbrava For?</h2>
    <svg class="aud-icon" style="left:228px;top:2700px" viewBox="0 0 20 20" fill="none" stroke="#222" stroke-width="1.2"><path d="M4 12V9a6 6 0 0 1 12 0v3"/><rect x="3" y="11" width="3" height="5" rx="1"/><rect x="14" y="11" width="3" height="5" rx="1"/><path d="M16 16c0 2-2 2.5-5 2.5"/></svg>
    <p class="aud-text" style="left:264px;top:2698px">Aspiring Customer Service Professionals in Hospitality, Leisure, and Tourism</p>
    <svg class="aud-icon" style="left:492px;top:2698px" viewBox="0 0 20 20" fill="none" stroke="#222" stroke-width="1.2"><path d="M5 12a3.5 3.5 0 0 1 1-6.8A4 4 0 0 1 14 5.2a3.5 3.5 0 0 1 1 6.8v3H5z"/><path d="M5 15h10"/></svg>
    <p class="aud-text" style="left:524px;top:2698px">Entry-Level Professionals (Students, Young Adults, Returning Citizens, etc.)</p>
    <svg class="aud-icon" style="left:228px;top:2767px" viewBox="0 0 20 20" fill="none" stroke="#222" stroke-width="1.2"><path d="M4 16l2-5 8-8 3 3-8 8z"/><path d="M4 16l3-1"/></svg>
    <p class="aud-text" style="left:264px;top:2765px">Mid-Career Professionals Seeking a Career Transition</p>
    <svg class="aud-icon" style="left:492px;top:2767px" viewBox="0 0 20 20" fill="none" stroke="#222" stroke-width="1.2"><rect x="4" y="5" width="12" height="8" rx="1"/><path d="M2 15h16"/></svg>
    <p class="aud-text" style="left:524px;top:2765px">Business Organizations Seeking Training for Their Teams</p>
  </section>

  <!-- bottom form -->
  <section class="signup">
    <div class="photo" role="img" aria-label="Grey stone texture" style="left:0;top:2920px;width:78px;height:406px;background:linear-gradient(180deg,#9a9794,#bdb9b5,#8f8b87)"></div>
    <div class="photo" role="img" aria-label="Two bakers smiling over bread in a kitchen" style="left:433px;top:2920px;width:506px;height:406px;background:linear-gradient(120deg,#6f665e 0%,#a5968a 35%,#4c4540 65%,#2f3a33 100%)"></div>
    <h2 class="abs" style="left:548px;top:3188px;font-family:'Barlow Semi Condensed',sans-serif;font-weight:400;font-size:28px;color:#fff">Who Is #Zumbrava For?</h2>
    <p class="abs" style="left:548px;top:3233px;width:320px;font-size:7.5px;line-height:14px;color:#fff">Ready to advance your career and achieve success in the booming hospitality, leisure, and tourism industry? Complete the form below to discover how #Zumbrava can promote you to the top of the industry!</p>
    <div class="form-panel" style="left:78px;top:2920px;width:355px;height:406px">
      <h2 style="left:42px;top:18px">Get Started!</h2>
      <p class="intro" style="left:42px;top:62px;width:240px">Craving a thriving, high-paying career in hospitality, leisure, or tourism? You're not alone.</p>
      <div class="field" style="left:42px;top:102px;width:276px;height:30px">Online Course Lead Magnet<span class="chev"></span></div>
      <div class="field" style="left:42px;top:149px;width:133px;height:30px">First Name</div>
      <div class="field" style="left:185px;top:149px;width:133px;height:30px">Last Name</div>
      <div class="field" style="left:42px;top:195px;width:276px;height:30px">Email</div>
      <div class="field" style="left:42px;top:241px;width:276px;height:30px">Phone</div>
      <p class="note" style="left:42px;top:282px">Craving a thriving, high-paying career in hospitality</p>
      <div class="btn" style="left:42px;top:305px;width:276px;height:31px">Learn More</div>
      <p class="fine" style="left:42px;top:350px;width:276px">Craving a thriving, high-paying career in hospitality, leisure, or tourism? You're not alone. With millions of new jobs on the horizon, opportunities in the hospitality industry have never been more promising.</p>
    </div>
  </section>

  <!-- footer -->
  <footer>
    <div class="brand-mark" style="left:78px;top:3364px"><span class="sq"></span>Zumbrava</div>
    <p class="abs" style="right:90px;top:3370px;font-size:7.5px;color:var(--text)">© 2024 Zumbrava. All rights reserved.</p>
  </footer>

</main>
</body>
</html>
```